Business Card Design Project

Looking for a logo and business card for a Real State Business i will be opening. The name is not choosen yet , but will probably be RTV IMOVEIS.
I was thinking black and silver colors, but am open to nice ideas.
I did add a business card that i liked a lot, am looking for something like that, with logo in black or silver in a black card. The logo i was thinking in the letters RTV as i uploaded or something or little and cute buildings or a house...just ideas, can be any nice logo.
Updates

You guys can add other colors if you want, I like colors very "BRIGHT" and "open", like red, pink, strong colors. almost glow in the dark colors. lol

Designers,

I've increased more 88 dollars in the budget for 1st place cause I will want envelope designs... small and big sizes.

So 1st place is now U$248,00. 

No need to send the envelope designs right now... only the business cards designs.

Thank you.

Industry/Entity Type

Business

Requirements
Must have
• Renata Tavares Vilela

www.RTVimoveis-exemplo.com.br

+554188316402

renata@rtvimoveis-exemplo.com.br

```html
<!DOCTYPE html>
<html lang="pt-BR">
<head>
<meta charset="utf-8">
<title>RTV Imoveis – Business Card</title>
<link rel="stylesheet" href="https://fonts.googleapis.com/css2?family=Poppins:wght@400;700&display=swap">
<style>
  :root {
    --backdrop: #4a4a4a;
    --card: #231f20;
    --pink: #ec008c;
    --white: #ffffff;
  }
  * { margin: 0; padding: 0; box-sizing: border-box; }
  html, body { width: 1200px; height: 892px; overflow: hidden; }
  body {
    background: var(--backdrop);
    font-family: "Poppins", sans-serif;
    position: relative;
  }
  .card {
    position: absolute;
    width: 580px;
    height: 340px;
    background: var(--card);
    overflow: hidden;
  }
  /* Front */
  .card-front { left: 580px; top: 50px; }
  .brand-lockup {
    position: absolute;
    inset: 0;
    display: flex;
    flex-direction: column;
    align-items: center;
    justify-content: center;
    color: var(--pink);
    font-weight: 700;
    line-height: 0.9;
  }
  .brand-initials { font-size: 150px; letter-spacing: -4px; }
  .brand-word { font-size: 66px; letter-spacing: 1px; }

  /* Back */
  .card-back { left: 40px; top: 500px; }
  .side-initials {
    position: absolute;
    left: 2px;
    top: -14px;
    display: flex;
    flex-direction: column;
    color: var(--pink);
    font-weight: 700;
    font-size: 128px;
    line-height: 0.9;
  }
  .divider { position: absolute; inset: 0; width: 580px; height: 340px; }
  .contact {
    position: absolute;
    left: 232px;
    top: 118px;
    color: var(--white);
  }
  .contact-name { color: var(--pink); font-weight: 700; font-size: 15px; }
  .contact-role { font-size: 12px; margin-top: 2px; }
  .contact-list { list-style: none; margin-top: 22px; font-size: 14px; }
  .contact-list li { display: flex; align-items: center; gap: 8px; line-height: 1.45; }
  .contact-list svg { width: 14px; height: 12px; fill: var(--pink); }
  .contact-web { font-size: 17px; margin-top: 2px; }
</style>
</head>
<body>
  <section class="card card-front" aria-label="Card front">
    <div class="brand-lockup">
      <span class="brand-initials">RTV</span>
      <span class="brand-word">IMOVEIS</span>
    </div>
  </section>

  <section class="card card-back" aria-label="Card back">
    <div class="side-initials" aria-label="RTV">
      <span>R</span><span>T</span><span>V</span>
    </div>
    <svg class="divider" viewBox="0 0 580 340" aria-hidden="true">
      <line x1="205" y1="0" x2="275" y2="104" stroke="#fff" stroke-width="2.5"/>
      <line x1="392" y1="250" x2="452" y2="340" stroke="#fff" stroke-width="2.5"/>
    </svg>
    <div class="contact">
      <p class="contact-name">Renata Tavares Vilela</p>
      <p class="contact-role">Real State Agent</p>
      <ul class="contact-list">
        <li>
          <svg viewBox="0 0 14 12"><path d="M1 4 C1 1 13 1 13 4 L10.5 5 L9.5 3.5 L4.5 3.5 L3.5 5 Z M3 6 L11 6 L12 11 L2 11 Z"/></svg>
          +55 4188 316 402
        </li>
        <li>
          <svg viewBox="0 0 14 12"><path d="M1 2 H13 V11 H1 Z M1.5 2.5 L7 7 L12.5 2.5" stroke="#231f20" stroke-width="1"/></svg>
          renata@rtvimoveis-exemplo.com.br
        </li>
        <li class="contact-web">www.RTVimoveis-exemplo.com.br</li>
      </ul>
    </div>
  </section>
</body>
</html>
```